Pet Shop Website

website will need to have the following features:
• Photo Galleries of each species (Dogs, Cats, Birds, Fish, Reptiles, Rabbits) in a light box popup
o Each species may have several different categories for example:
 Fish
• Marine fish
• Fresh water
• tropical
• Cichlid
• Information Fact sheets of each species – Downloaded as a pdf which can be either
o Care Sheets
o Training Sheets
• Members Area
o Username (Email Address) & Password login
o New signups
o Exclusive Member Deals
o Newsletter options

The front page must be very simple (for example lumavest.com.au) contain the following:
• Product of the week - which can be purchased online
o Short details
o Cost
• Pet Club Sign up picture
• Animal of the week/month
• Contact Phone Number and addresses of the stores
• A jQuery slideshow (Images could include stores, pets etc…)
The main page MUST keep simple. We do not want it cluttered.

Inner Page
The animals / reptile page will need to have:
• Short description of the species
• Photo Galleries
• A list of what is in stock and the list needs to clearly be sorted by each store (Use of Tabs maybe).
• Facts sheets / Info sheets
The type of website ideas (not the type of look that we are necessary after) is and the sort of content that we want to offer are as follows:

http://www.scalenook.com.au/
http://www.brindlecovepaws.com.au/
http://www.thefurrowden.com.au
http://www.tailtown.net.au

Colour in the new website:
Blue
Red
Grey
Yellow

Original site:

http://www.critterglow.com.au
Updates

Hi Guys,

We had feedback from the client and they would like to see a few dark designs.

Thanks                                   

Reason: We would like to reopen this contest back up for a further week

Target Market(s)

Targeting animal lovers

Industry/Entity Type

Store

Requirements
Should not have
• Alter the logo in anyway

```html
<!DOCTYPE html>
<html lang="en">
<head>
<meta charset="utf-8">
<title>Critter Glow – Pet Superstores</title>
<link href="https://fonts.googleapis.com/css2?family=Arimo:wght@400;700&family=Open+Sans:wght@400;600&display=swap" rel="stylesheet">
<style>
:root{
  --page:#f4f4f4;
  --red:#c0393b;
  --red-dark:#a82a2d;
  --blue:#4a54a8;
  --blue-dark:#3b4497;
  --title-blue:#2a3aa8;
  --text:#555;
  --footer:#3f3f3f;
  --footer-strip:#353535;
  --connect:#cfe3f1;
  --accent-red:#c4302f;
  --muted:#999;
}
*{box-sizing:border-box;margin:0;padding:0}
html,body{width:1127px;height:1200px;overflow:hidden;background:var(--page)}
body{font-family:"Arimo",Arial,sans-serif;color:var(--text)}
.stage{position:relative;width:1150px;height:1224px;transform:scale(0.98);transform-origin:0 0}
.abs{position:absolute}

/* utility bar */
.utility{top:22px;left:403px;display:flex;gap:20px;font-size:13px;color:#444;align-items:center}
.utility span.sep{color:#666}
.utility .ico{display:inline-block;width:12px;height:11px;margin-right:6px;vertical-align:-1px}
.search{top:17px;left:830px;width:224px;height:29px;background:#fff;border:1px solid #ccc;border-radius:2px;font-size:11px;font-style:italic;color:#aaa;padding:8px 10px}
.search svg{position:absolute;right:14px;top:8px}

/* header */
.header{top:62px;left:88px;width:972px;height:96px;background:linear-gradient(#fff,#f7f7f7)}
.brand{top:88px;left:100px;display:flex;align-items:center;gap:10px;font-size:30px;font-weight:700;color:var(--blue-dark)}
.brand i{width:22px;height:22px;background:#f2cf2a;display:block}
.club-photo{top:86px;left:796px;width:100px;height:72px;border-radius:50% 50% 0 0;background:linear-gradient(#9d8a72,#5e4d3d)}
.club-card{top:99px;left:896px;width:164px;height:55px;background:#f1f1f1;border-radius:0 6px 0 0;padding:9px 0 0 10px;white-space:nowrap}
.club-card small{font-size:13px;color:#666;display:block}
.club-card b{font-weight:400;font-size:16px;color:var(--accent-red);display:block;margin-top:3px}

/* nav */
.nav{top:158px;left:88px;width:972px;height:54px;background:linear-gradient(var(--red),var(--red-dark));display:flex;border-bottom:3px solid #b13335}
.nav a{color:#fff;text-decoration:none;font-size:14px;padding:0 28px;line-height:54px;border-right:1px solid rgba(0,0,0,.18)}
.nav a.current{background:rgba(0,0,0,.1)}
.login-input{top:170px;width:144px;height:28px;background:#fff;border:1px solid #ddd;font-size:11px;font-style:italic;color:#aaa;padding:7px 10px}
.login-btn{top:169px;left:995px;width:54px;height:28px;background:linear-gradient(#fafafa,#ddd);border:1px solid #bbb;font-size:13px;font-style:italic;color:#444;text-align:center;line-height:26px;border-radius:2px}

/* slider */
.slider{top:220px;left:88px;width:972px;height:282px;background:#fff}
.slide{top:224px;left:92px;width:962px;height:274px;background:linear-gradient(90deg,#e6e6e6,#d9d9d9)}
.slide-photo{top:224px;left:440px;width:614px;height:274px;background:radial-gradient(ellipse at 55% 60%,#8a6a48,#b5a08a 45%,#dcdcdc 75%)}
.slide-text{top:268px;left:138px;font-size:22px;line-height:34px;color:#333}
.slide-text em{font-style:normal;color:var(--accent-red)}
.view-more{top:376px;left:140px;padding:6px 10px;background:#3e3e3e;color:#fff;font-size:12px;border-radius:4px}
.dots{top:466px;left:116px;display:flex;gap:11px}
.dots i{width:10px;height:10px;border-radius:50%;background:#666;display:block}
.dots i:first-child{background:var(--accent-red)}

/* welcome */
.welcome-title{top:534px;left:96px;font-size:20px;color:var(--title-blue)}
.welcome-copy{top:573px;left:97px;width:684px;font-size:12.6px;line-height:22px;color:#555}
.facts{top:541px;left:802px;width:250px;height:114px;background:#f6f6f6;border:1px solid #ddd;border-radius:3px}
.facts-photo{top:556px;left:818px;width:74px;height:80px;border-radius:40%;background:linear-gradient(#e2c8a4,#c49c6b)}
.pdf-icon{top:554px;left:907px;width:26px;height:31px;background:#fff;border:1px solid #ccc}
.pdf-icon span{position:absolute;bottom:2px;left:2px;background:var(--accent-red);color:#fff;font-size:7px;padding:0 2px}
.facts-link{top:560px;left:945px;font-size:13px;color:var(--title-blue);text-decoration:underline}
.facts-text{top:594px;left:905px;font-size:14.5px;line-height:20px;color:var(--accent-red)}

/* cards */
.card{top:698px;width:292px;height:282px;background:#fff;border:1px solid #e3e3e3;border-radius:4px;box-shadow:0 1px 3px rgba(0,0,0,.08)}
.card-head{height:50px;background:linear-gradient(var(--blue),var(--blue-dark));border-radius:4px 4px 0 0;color:#fff;font-size:18px;padding:14px 22px;position:relative}
.card-arrows{position:absolute;right:14px;top:17px;display:flex;gap:3px}
.card-arrows i{width:13px;height:15px;background:#c9cbe3;border-radius:7px;display:block}
.card-photo{position:absolute;top:64px;left:12px;width:128px;height:148px;border-radius:40%}
.card-info{position:absolute;top:70px;left:154px;font-size:14.5px}
.card-info .name{color:#333}
.card-info .breed{color:var(--muted);margin-top:6px}
.card-info .price{color:var(--accent-red);margin-top:13px}
.cart-btn{position:absolute;top:156px;left:152px;width:122px;height:31px;background:linear-gradient(#6a6a6a,#4a4a4a);border-radius:16px;color:#fff;font-size:13px;line-height:31px;padding-left:42px}
.cart-btn svg{position:absolute;left:17px;top:8px}
.select{position:absolute;top:228px;left:30px;width:224px;height:28px;border:1px solid #ccc;border-radius:2px;font-size:11px;font-style:italic;color:#aaa;padding:7px 16px}
.select::after{content:"▾";position:absolute;right:12px;top:6px;font-style:normal;color:#555;font-size:10px}
.wide-btn{position:absolute;top:228px;left:34px;width:223px;height:28px;background:linear-gradient(#555,#333);color:#fff;font-size:13px;line-height:28px;text-align:center}
.wide-btn b{display:inline-block;width:13px;height:13px;border-radius:50%;background:#777;margin-left:10px;vertical-align:-2px}

/* footer */
.footer{top:1043px;left:95px;width:939px;height:181px;background:var(--footer)}
.footer-strip{top:1180px;left:95px;width:939px;height:44px;background:var(--footer-strip)}
.connect{top:1012px;left:124px;width:910px;height:65px;background:var(--connect);font-family:"Open Sans",sans-serif;font-size:15px;color:#333}
.connect .label{position:absolute;top:22px;left:27px}
.socials{position:absolute;top:18px;left:165px;display:flex;gap:12px}
.socials i{width:26px;height:26px;display:block;border-radius:2px}
.connect .divider{position:absolute;left:418px;top:6px;width:1px;height:54px;background:#9fb6c7}
.connect .news{position:absolute;left:446px;top:22px}
.mail-input{position:absolute;left:546px;top:17px;width:200px;height:28px;background:#fff;border:1px solid #aac;font-size:11px;font-style:italic;color:#aaa;text-align:center;line-height:26px}
.subscribe{position:absolute;left:761px;top:18px;width:112px;height:26px;background:#2f2f2f;color:#fff;font-size:14px;text-align:center;line-height:26px;border-radius:2px}
.store{top:1097px;font-family:"Open Sans",sans-serif;font-size:12px;color:#e6e6e6;line-height:24px;white-space:nowrap}
.store h4{font-weight:400;text-transform:uppercase}
.payments{top:1097px;left:818px;font-family:"Open Sans",sans-serif;font-size:12px;color:#e6e6e6}
.cards-row{display:flex;gap:7px;margin-top:14px}
.cards-row i{width:29px;height:19px;background:#f2f2f2;border-radius:2px;display:block}
.footer-links{top:1193px;left:126px;font-family:"Open Sans",sans-serif;font-size:12px;color:#ddd}
.footer-links span{color:#888;margin:0 5px}
.copyright{top:1193px;left:600px;width:433px;text-align:right;white-space:nowrap;font-family:"Open Sans",sans-serif;font-size:12px;color:#ddd}
</style>
</head>
<body>
<div class="stage">

  <div class="abs utility">
    <span><svg class="ico" viewBox="0 0 12 11"><circle cx="6" cy="3" r="3" fill="#555"/><path d="M0 11c0-4 12-4 12 0z" fill="#555"/></svg>My Account</span><span class="sep">|</span>
    <span><svg class="ico" viewBox="0 0 12 11"><path d="M0 1h2l2 6h7l1-5H3" fill="none" stroke="#555" stroke-width="1.3"/><circle cx="5" cy="9.5" r="1.2" fill="#555"/><circle cx="10" cy="9.5" r="1.2" fill="#555"/></svg>My Cart</span><span class="sep">|</span>
    <span><svg class="ico" viewBox="0 0 12 11"><rect x=".5" y="1" width="10" height="9.5" fill="none" stroke="#555"/><path d="M3 5l2 2 6-6" fill="none" stroke="#555" stroke-width="1.4"/></svg>Check out</span><span class="sep">|</span>
    <span>? Help</span>
  </div>
  <div class="abs search">Search here...
    <svg width="12" height="12" viewBox="0 0 12 12"><circle cx="5" cy="5" r="3.5" fill="none" stroke="#bbb" stroke-width="1.4"/><path d="M8 8l3 3" stroke="#bbb" stroke-width="1.6"/></svg>
  </div>

  <div class="abs header"></div>
  <div class="abs brand"><i></i>Critter Glow</div>
  <div class="abs club-photo" role="img" aria-label="Kitten peeking over the edge"></div>
  <div class="abs club-card"><small>Click here for</small><b>Sign up for Pet Club</b></div>

  <nav class="abs nav">
    <a class="current" href="#">HOME</a><a href="#">ABOUT US</a><a href="#">PETS</a><a href="#">GALLERY</a><a href="#">CONTACT US</a>
  </nav>
  <div class="abs login-input" style="left:693px">username</div>
  <div class="abs login-input" style="left:844px">********</div>
  <div class="abs login-btn">Log in</div>

  <div class="abs slider"></div>
  <div class="abs slide"></div>
  <div class="abs slide-photo" role="img" aria-label="Group of four dogs sitting together"></div>
  <div class="abs slide-text">Welcome to Critter Glow your<br><em>PET SUPERSTORES</em> at<br>Harlow Vale and Wren Point</div>
  <div class="abs view-more">View more</div>
  <div class="abs dots"><i></i><i></i><i></i><i></i></div>

  <h2 class="abs welcome-title" style="font-weight:400">Welcome to our site</h2>
  <p class="abs welcome-copy">Sed tempus lectus ut arcu consectetur at tempor justo imperdiet. Maecenas eu ligula nisl. Donec placerat mollis odio, eu pulvinar arcu eleifend nec. Sed vulputate turpis libero, vel pharetra nulla. Cras ut pretium turpis. Nunc pharetra tortor nec ipsum consequat sit amet imperdiet nibh suscipit. Fusce posuere, neque eu mattis iaculis, dolor ipsum semper velit, in posuere velit orci sit amet libero. Integer sollicitudin facilisis purus vitae aliquet. Etiam elit quam</p>

  <div class="abs facts"></div>
  <div class="abs facts-photo" role="img" aria-label="Rabbit"></div>
  <div class="abs pdf-icon"><span>PDF</span></div>
  <div class="abs facts-link">Download here</div>
  <div class="abs facts-text">Download our lates<br>Fact sheets</div>

  <section class="abs card" style="left:100px">
    <div class="card-head">Our Gallery<div class="card-arrows"><i></i><i></i></div></div>
    <div class="card-photo" role="img" aria-label="Small white dog holding a red heart toy" style="background:radial-gradient(#eee5da,#c8b39b 70%,#fff 72%)"></div>
    <div class="card-info"><div class="name">Pet Name</div><div class="breed">Breed Type</div><div class="price">Price : $00.00</div></div>
    <div class="cart-btn"><svg width="16" height="13" viewBox="0 0 12 11"><path d="M0 1h2l2 6h7l1-5H3" fill="none" stroke="#fff" stroke-width="1.3"/><circle cx="5" cy="9.5" r="1.2" fill="#fff"/><circle cx="10" cy="9.5" r="1.2" fill="#fff"/></svg>Add to cart</div>
    <div class="select">Dogs</div>
  </section>

  <section class="abs card" style="left:429px">
    <div class="card-head">Exclusive Member Deals<div class="card-arrows"><i></i><i></i></div></div>
    <div class="card-photo" role="img" aria-label="Grey tabby kitten sitting" style="background:radial-gradient(#c9c9c9,#9a9a9a 60%,#fff 72%)"></div>
    <div class="card-info"><div class="name">Pet Name</div><div class="breed">Breed Type</div><div class="price">Offer : 18 %</div></div>
    <div class="cart-btn"><svg width="16" height="13" viewBox="0 0 12 11"><path d="M0 1h2l2 6h7l1-5H3" fill="none" stroke="#fff" stroke-width="1.3"/><circle cx="5" cy="9.5" r="1.2" fill="#fff"/><circle cx="10" cy="9.5" r="1.2" fill="#fff"/></svg>Add to cart</div>
    <div class="wide-btn">View more about this Deal<b></b></div>
  </section>

  <section class="abs card" style="left:758px">
    <div class="card-head">Product of the week<div class="card-arrows"><i></i><i></i></div></div>
    <div class="card-photo" role="img" aria-label="Guinea pig" style="background:radial-gradient(#f4ece2,#d8994d 65%,#fff 72%)"></div>
    <div class="card-info"><div class="name">Pet Name</div><div class="breed">Breed Type</div><div class="price">Price : $00.00</div></div>
    <div class="cart-btn"><svg width="16" height="13" viewBox="0 0 12 11"><path d="M0 1h2l2 6h7l1-5H3" fill="none" stroke="#fff" stroke-width="1.3"/><circle cx="5" cy="9.5" r="1.2" fill="#fff"/><circle cx="10" cy="9.5" r="1.2" fill="#fff"/></svg>Add to cart</div>
    <div class="wide-btn">Sign up/ Sign in for more<b></b></div>
  </section>

  <footer>
    <div class="abs footer"></div>
    <div class="abs footer-strip"></div>
    <div class="abs connect">
      <span class="label">Connect with us :</span>
      <div class="socials">
        <i style="background:#3b5a9a"></i><i style="background:#36a9d9"></i><i style="background:#2f2f2f"></i><i style="background:#f29a1f"></i><i style="background:#c9302c"></i><i style="background:#7b98ab"></i>
      </div>
      <div class="divider"></div>
      <span class="news">News Letter</span>
      <div class="mail-input">Enter your mail ID</div>
      <div class="subscribe">Subscribe</div>
    </div>

    <div class="abs store" style="left:127px">
      <h4>Harlow Vale Superstore</h4>
      <div>Shop 4 / 220 Marlin Rd, HARLOW VALE, W.A 6190</div>
      <div>Ph : (08) 9300 1200 &nbsp; | &nbsp; Fax : (08) 9300 1210</div>
    </div>
    <div class="abs store" style="left:487px">
      <h4>Wren Point Superstore</h4>
      <div>Unit 3 / 18 Tidewell Drive, &nbsp;WREN POINT, W.A 6172</div>
      <div>Ph : (08) 9300 4400 &nbsp; | &nbsp; Fax : &nbsp;(08) 9300 4410</div>
    </div>
    <div class="abs payments">Payments
      <div class="cards-row"><i></i><i></i><i></i><i></i><i></i></div>
    </div>

    <div class="abs footer-links">Home<span>|</span>About us<span>|</span>Pets<span>|</span>Gallery<span>|</span>Contact Us</div>
    <div class="abs copyright">Copyright © www.critterglow.com.au &nbsp; All rights reserved.</div>
  </footer>

</div>
</body>
</html>
```